Crafted Ember Website

Would like a website designed for my fitness and nutrition coaching company Craft Ember. I have a company logo and would like to keep the page layout clean and simple. Needs to look great on computer and mobile devices.

Target Market(s)

Target market is individuals looking to make changes in their health and nutrition with the help of an online coach.

Industry/Entity Type

Fitness

Number of Pages Required

2 page

Colors
3176b5
0355a3
85acd3
cedeed
f8fcfd
ffffff

Requirements
Must have
• The first page should have the company logo and name towards the top and below that client before and after photos scrolling or displaying in some manner. Also would like a section that states services offered and a section about myself since I am the primary coach for clients.

```html
<!DOCTYPE html>
<html lang="en">
<head>
<meta charset="utf-8">
<title>Crafted Ember — Fitness &amp; Wellness</title>
<link rel="stylesheet" href="https://fonts.googleapis.com/css2?family=Jost:wght@400;500;600&family=Roboto+Condensed:wght@400;700&family=Open+Sans:wght@400;600&family=Oswald:wght@600&display=swap">
<style>
:root{
  --blue:#3176b5;
  --blue-deep:#0355a3;
  --blue-mid:#85acd3;
  --blue-pale:#cedeed;
  --snow:#f8fcfd;
  --white:#ffffff;
  --ink:#1d1d1f;
  --grey:#6b6f75;
  --footer:#28333f;
  --footer-deep:#1e2731;
  --heading:'Jost',sans-serif;
  --cond:'Roboto Condensed',sans-serif;
  --body:'Open Sans',sans-serif;
}
*{box-sizing:border-box;margin:0;padding:0}
html,body{width:1200px;height:2667px;overflow:hidden;background:var(--white)}
.page{position:relative;width:1200px;height:2667px;font-family:var(--body);color:var(--ink)}
.abs{position:absolute}

/* top bar */
.topbar{left:0;top:0;width:1200px;height:48px;background:var(--white)}
.topbar__login{left:158px;top:12px;font:400 17px var(--cond);color:var(--blue-deep);text-transform:uppercase}
.btn{display:flex;align-items:center;justify-content:center;background:var(--blue);color:var(--white);font:400 16px var(--cond);text-transform:uppercase;border-radius:3px}
.topbar__cta{left:912px;top:5px;width:128px;height:36px;background:var(--blue-deep)}

/* nav */
.nav{left:0;top:48px;width:1200px;height:107px;background:var(--blue-pale)}
.brand{display:flex;flex-direction:column;align-items:center}
.brand__mark{width:44px;height:44px;border:4px solid var(--blue)}
.brand__name{font:500 20px var(--heading);color:var(--blue);letter-spacing:.5px;text-transform:uppercase;margin-top:6px}
.nav .brand{left:158px;top:10px;width:190px}
.nav__links{left:748px;top:42px;display:flex;gap:36px;font:400 16px var(--cond);color:var(--blue-deep);text-transform:uppercase}

/* hero */
.hero{left:0;top:155px;width:1200px;height:476px;background:linear-gradient(100deg,#3a79b8 0%,#5b8fc4 35%,#4b82bd 60%,#3575b6 100%)}
.hero__title{left:0;width:1200px;top:88px;text-align:center;font:400 46px var(--cond);color:var(--white)}
.hero__slogan{left:0;width:1200px;top:160px;text-align:center;font:600 42px var(--heading);color:var(--white);text-decoration:underline;text-decoration-thickness:3px;text-underline-offset:8px;text-transform:uppercase}
.hero__points{left:0;width:1200px;top:262px;display:flex;justify-content:center;gap:44px;font:400 24px var(--cond);color:var(--white)}
.hero__points li{list-style:none;display:flex;align-items:center;gap:12px}
.hero__cta{left:528px;top:327px;width:142px;height:46px;font-size:17px;box-shadow:0 2px 4px rgba(0,0,0,.2)}
.price-badge{left:924px;top:574px;width:114px;height:114px;border-radius:50%;background:var(--blue-deep);border:3px solid var(--white);display:flex;flex-direction:column;align-items:center;justify-content:center;color:var(--white);font-family:var(--cond)}
.price-badge::after{content:"";position:absolute;inset:8px;border:1px dashed rgba(255,255,255,.7);border-radius:50%}
.price-badge small{font-size:15px}
.price-badge strong{font-size:19px}

/* intro */
.section-title{left:0;width:1200px;text-align:center;font:600 30px var(--heading);text-transform:uppercase;color:var(--ink);letter-spacing:.5px}
.intro__title{top:678px}
.quote{left:158px;top:766px;width:440px;font:400 14.5px/1.95 var(--body);color:var(--grey)}
.quote__mark{color:var(--blue);font:700 22px var(--heading)}
.quote__name{left:158px;top:918px;font:400 24px var(--cond);color:var(--ink)}
.quote__role{left:160px;top:950px;font:400 11.5px var(--body);color:var(--grey)}
.before-photo{left:686px;top:788px;width:146px;height:254px;border-radius:50%;border:2px solid var(--blue-deep);background:linear-gradient(180deg,#e6e3e0,#c7b3a5 45%,#6e8cb8)}
.after-photo{left:872px;top:770px;width:136px;height:316px;border-radius:60px 60px 20px 20px;background:linear-gradient(180deg,#f2f2f2,#d9c3b6 35%,#7392bf 65%,#5a7aab)}
.after-shadow{left:868px;top:1090px;width:140px;height:10px;border-radius:50%;background:#e2e2e2}
.kg-badge{left:637px;top:816px;width:78px;height:78px;border-radius:50%;background:var(--blue-deep);color:var(--white);display:flex;align-items:center;justify-content:center;font:700 30px var(--cond)}
.kg-badge sub{font-size:15px;vertical-align:-4px}
.label{font:700 16px var(--cond);color:var(--ink)}
.label--before{left:733px;top:1048px}
.label--after{left:955px;top:753px}

/* services */
.services{left:0;top:1168px;width:1200px;height:475px;background:var(--snow);border-top:1px solid #e6ecef}
.services__title{top:1207px}
.services__sub{left:0;width:1200px;top:1254px;text-align:center;font:400 20px var(--cond);color:var(--blue-deep)}
.service{top:1323px;width:320px;display:flex;flex-direction:column;align-items:center;text-align:center}
.service__photo{width:170px;height:170px;border-radius:50%}
.service__name{margin-top:28px;font:400 18px var(--cond);color:var(--ink)}
.service__text{margin-top:12px;font:400 13.5px/1.35 var(--body);color:var(--blue)}

/* about */
.about{left:0;top:1643px;width:1200px;height:345px;background:linear-gradient(90deg,#2f75bd 0%,#3a80c4 50%,#4d8ac8 75%,#3a7cc0 100%)}
.about__title{left:0;width:1200px;top:1686px;text-align:center;font:600 25px var(--heading);color:var(--white);text-transform:uppercase}
.about__rule{left:347px;top:1730px;width:515px;height:5px;background:rgba(255,255,255,.45)}
.about__photo{left:247px;top:1765px;width:196px;height:196px;border-radius:50%;border:4px solid var(--white);background:radial-gradient(circle at 45% 45%,#d8b39c,#a47a62 70%,#3b3b3f)}
.about__lead{left:487px;top:1766px;font:400 19px var(--cond);color:var(--white)}
.about__headline{left:489px;top:1818px;font:600 31px/1.25 'Oswald',sans-serif;color:var(--white);text-transform:uppercase}

/* testimonials */
.clients{left:0;top:1988px;width:1200px;height:389px;background:var(--snow)}
.clients__title{top:2040px;font-size:25px}
.review{left:364px;top:2142px;width:628px;height:148px;background:var(--white);box-shadow:0 1px 6px rgba(0,0,0,.12)}
.review__avatar{left:215px;top:2121px;width:182px;height:182px;border-radius:50%;background:linear-gradient(180deg,#dedfe2,#b7b2ae 50%,#8d8f95)}
.review__name{left:420px;top:2163px;font:400 19px var(--cond);color:var(--blue-deep);text-transform:uppercase}
.review__text{left:420px;top:2195px;width:540px;font:400 12.5px/1.85 var(--body);color:var(--grey)}
.review__more{left:420px;top:2253px;font:600 12.5px var(--body);color:var(--ink)}
.dots{left:578px;top:2326px;display:flex;gap:6px}
.dots span{width:10px;height:10px;border-radius:50%;background:var(--blue-pale)}
.dots span:first-child{background:var(--blue-deep)}

/* footer */
.footer{left:0;top:2377px;width:1200px;height:256px;background:var(--footer)}
.footer__head{font:400 19px var(--cond);color:var(--white);padding-bottom:8px;border-bottom:1px solid #4a5663;width:118px}
.footer__col--links{left:158px;top:2404px}
.footer__col--lang{left:356px;top:2404px}
.footer__list{list-style:none;margin-top:12px;font:400 16px/1.45 var(--cond);color:var(--white)}
.flag{display:inline-block;width:22px;height:14px;background:linear-gradient(180deg,#c8102e 0 50%,#1f3a8a 50%);vertical-align:-2px;margin-right:10px}
.footer__help{left:556px;top:2436px;width:157px;height:44px;font-size:17px}
.footer .brand{left:810px;top:2410px;width:230px}
.footer .brand__mark{width:58px;height:58px}
.footer .brand__name{font-size:23px;margin-top:14px}
.social{left:855px;top:2562px;display:flex;gap:12px}
.social span{width:36px;height:36px;border-radius:50%;background:#5f6770}
.copyright{left:0;top:2633px;width:1200px;height:34px;background:var(--footer-deep);display:flex;align-items:center;justify-content:center;font:400 11px var(--body);color:#9aa3ad}
.copyright b{color:var(--blue-mid);font-weight:400;margin:0 4px}
</style>
</head>
<body>
<div class="page">

  <header class="topbar abs">
    <a class="topbar__login abs">Login or Create an Account</a>
    <a class="topbar__cta btn abs">Get Startted</a>
  </header>

  <nav class="nav abs">
    <div class="brand abs"><span class="brand__mark"></span><span class="brand__name">Crafted Ember</span></div>
    <ul class="nav__links abs" style="list-style:none"><li>Home</li><li>Consulting</li><li>Testimonial</li></ul>
  </nav>

  <section class="hero abs" role="img" aria-label="Blue-toned photo of a woman measuring her waist with a tape measure by the sea">
    <h1 class="hero__title abs">FITNESS &amp; WELLNESS</h1>
    <p class="hero__slogan abs">Love Our Health</p>
    <ul class="hero__points abs">
      <li><svg width="20" height="20" viewBox="0 0 20 20"><circle cx="10" cy="10" r="8.5" fill="none" stroke="#fff" stroke-width="1.6"/><path d="M5.5 10h8M10 6.5l3.5 3.5-3.5 3.5" fill="none" stroke="#fff" stroke-width="1.6"/></svg>Nutrition</li>
      <li><svg width="20" height="20" viewBox="0 0 20 20"><circle cx="10" cy="10" r="8.5" fill="none" stroke="#fff" stroke-width="1.6"/><path d="M5.5 10h8M10 6.5l3.5 3.5-3.5 3.5" fill="none" stroke="#fff" stroke-width="1.6"/></svg>Fitness</li>
      <li><svg width="20" height="20" viewBox="0 0 20 20"><circle cx="10" cy="10" r="8.5" fill="none" stroke="#fff" stroke-width="1.6"/><path d="M5.5 10h8M10 6.5l3.5 3.5-3.5 3.5" fill="none" stroke="#fff" stroke-width="1.6"/></svg>Motivation</li>
    </ul>
    <a class="hero__cta btn abs">Learn More</a>
  </section>
  <div class="price-badge abs"><small>in Just</small><strong>$ 9,605</strong></div>

  <h2 class="section-title intro__title abs">Crafted Ember</h2>
  <blockquote class="quote abs"><span class="quote__mark">&ldquo;</span> Lorem ipsum dolor sit amet, consectetur adipiscing elit, sed do eiusmod tempor incididunt ut labore et dolore magna aliqua. Ut enim ad minim veniam... <span class="quote__mark">&rdquo;</span></blockquote>
  <p class="quote__name abs">- Mara Delvin</p>
  <p class="quote__role abs">Lorem Ipsum Dolor Sit Amet</p>

  <div class="before-photo abs" role="img" aria-label="Client before photo"></div>
  <div class="after-shadow abs"></div>
  <div class="after-photo abs" role="img" aria-label="Client after photo"></div>
  <div class="kg-badge abs">15<sub>kg</sub></div>
  <svg class="abs" style="left:780px;top:990px" width="100" height="70" viewBox="0 0 100 70"><path d="M4 40 C 30 75, 70 68, 86 16" fill="none" stroke="#555" stroke-width="1.4" stroke-dasharray="4 3"/><path d="M78 20 L87 10 L90 24" fill="none" stroke="#555" stroke-width="1.4"/></svg>
  <span class="label label--before abs">Before</span>
  <span class="label label--after abs">After</span>

  <section class="services abs"></section>
  <h2 class="section-title services__title abs">Crafted Ember Services</h2>
  <p class="services__sub abs">Lorem Ipsum Dolor Ist Amet</p>
  <div class="service abs" style="left:119px">
    <div class="service__photo" role="img" aria-label="Woman in sportswear drinking water" style="background:linear-gradient(160deg,#eef1f3,#c9a9a5 55%,#b85c90)"></div>
    <p class="service__name">Services - 1</p>
    <p class="service__text">Lorem Ipsum Dolor Sit Amet Consect<br>Consectetor Lorem Ipsum</p>
  </div>
  <div class="service abs" style="left:439px">
    <div class="service__photo" role="img" aria-label="Woman holding a bowl of salad" style="background:linear-gradient(160deg,#a9c86a,#f3f1ec 50%,#c9dbe0)"></div>
    <p class="service__name">Services - 2</p>
    <p class="service__text">Lorem Ipsum Dolor Sit Amet Consect<br>Consectetor Lorem Ipsum</p>
  </div>
  <div class="service abs" style="left:761px">
    <div class="service__photo" role="img" aria-label="Waist wrapped with a measuring tape" style="background:linear-gradient(180deg,#d8b6a2,#c98f7c 55%,#c2334a)"></div>
    <p class="service__name">Services - 3</p>
    <p class="service__text">Lorem Ipsum Dolor Sit Amet Consect<br>Consectetor Lorem Ipsum</p>
  </div>

  <section class="about abs" role="img" aria-label="Blue-toned kitchen scene with a woman in sportswear"></section>
  <h2 class="about__title abs">About Crafted Ember</h2>
  <div class="about__rule abs"></div>
  <div class="about__photo abs" role="img" aria-label="Toned abdomen of the coach"></div>
  <p class="about__lead abs">Lorem Ipsum Dolor Sit Amet Consectetor</p>
  <p class="about__headline abs">Tips from award winning<br>Crafted Ember</p>

  <section class="clients abs"></section>
  <h2 class="section-title clients__title abs">What our client says</h2>
  <div class="review abs"></div>
  <div class="review__avatar abs" role="img" aria-label="Client portrait holding dumbbells"></div>
  <p class="review__name abs">Tessa Varga</p>
  <p class="review__text abs">"Lorem ipsum dolor sit amet, consectetur adipiscing elit, sed do eiusmod tempor incididunt ut labore et dolore magna aliqua. Ut enim ad minim veniam, quis nostrud exercitation...</p>
  <p class="review__more abs">Read More</p>
  <div class="dots abs"><span></span><span></span><span></span></div>

  <footer class="footer abs">
  </footer>
  <div class="footer__col--links abs">
    <p class="footer__head">Quick Link</p>
    <ul class="footer__list"><li>Home</li><li>About Us</li><li>Consulting</li><li>Testimonials</li></ul>
  </div>
  <div class="footer__col--lang abs">
    <p class="footer__head">Language</p>
    <ul class="footer__list"><li><span class="flag"></span>English</li></ul>
  </div>
  <a class="footer__help btn abs">Need Help!</a>
  <div class="footer abs" style="background:none;height:0"><div class="brand abs"><span class="brand__mark"></span><span class="brand__name">Crafted Ember</span></div></div>
  <div class="social abs"><span></span><span></span><span></span></div>
  <div class="copyright abs">Copyrights©2017<b>Crafted Ember</b>Allrights are reserved.</div>

</div>
</body>
</html>
```